Business card and stationery
Sun "N" Sail Clam Bar & Grill
Professional
Dale Pritchard
1187 North Cedar Row
Harbor Vale, CA. 90417
Daltonpritchard@quillmail.com
Leave room for: phone number, fax, email and web address

```html
<!DOCTYPE html>
<html lang="en">
<head>
<meta charset="utf-8">
<title>Sun "N" Sail Clam Bar &amp; Grill – Business Cards</title>
<link href="https://fonts.googleapis.com/css2?family=Open+Sans:wght@400;700&display=swap" rel="stylesheet">
<style>
  :root{
    --bg:#ecebe8;
    --navy:#1f3a7a;
    --orange:#f28a26;
    --orange-light:#fbbd72;
    --ink:#55585e;
    --rule:#c9ccd3;
    --card-white:#ffffff;
    --card-grey:#e9e9ea;
  }
  *{margin:0;padding:0;box-sizing:border-box}
  html,body{width:1200px;height:811px;overflow:hidden}
  body{background:var(--bg);font-family:"Open Sans",Arial,sans-serif;position:relative}

  .card{position:absolute;border-radius:16px;overflow:hidden;box-shadow:0 4px 12px rgba(0,0,0,.18)}
  .card--front-orange{left:139px;top:53px;width:449px;height:312px;
    background:radial-gradient(ellipse at 45% 45%,var(--orange-light) 0%,var(--orange) 100%)}
  .card--front-white{left:610px;top:53px;width:449px;height:312px;
    background:radial-gradient(ellipse at 50% 45%,var(--card-white) 0%,var(--card-grey) 100%)}
  .card--back{left:329px;top:415px;width:542px;height:315px;background:var(--card-white);border-radius:12px}

  .brand{position:absolute;left:0;right:0;text-align:center;color:var(--navy);font-weight:700;line-height:1.1}
  .card--front-orange .brand,.card--front-white .brand{top:102px}
  .brand__name{display:block;font-size:40px;letter-spacing:1px}
  .brand__tag{display:block;font-size:24px;margin-top:8px}
  .card--back .brand{top:30px}
  .card--back .brand__name{font-size:26px}
  .card--back .brand__tag{font-size:15px;margin-top:4px}

  .holder{position:absolute;left:22px;top:168px;font-size:20px;font-weight:700;color:var(--navy)}
  .address{position:absolute;left:22px;top:212px;font-size:11px;line-height:1.6;color:var(--ink);display:flex;gap:8px}
  .divider{position:absolute;left:271px;top:160px;width:1px;height:112px;background:var(--rule)}
  .contact{position:absolute;left:300px;top:172px;list-style:none;font-size:11px;color:var(--ink)}
  .contact li{display:flex;align-items:center;gap:7px;height:19px}
  .icon{width:11px;height:11px;flex:none}
  .bands{position:absolute;left:0;bottom:0}
</style>
</head>
<body>

<section class="card card--front-orange">
  <div class="brand"><span class="brand__name">SUN "N" SAIL</span><span class="brand__tag">Clam Bar &amp; Grill</span></div>
</section>

<section class="card card--front-white">
  <div class="brand"><span class="brand__name">SUN "N" SAIL</span><span class="brand__tag">Clam Bar &amp; Grill</span></div>
</section>

<section class="card card--back">
  <div class="brand"><span class="brand__name">SUN "N" SAIL</span><span class="brand__tag">Clam Bar &amp; Grill</span></div>

  <h1 class="holder">Dale Pritchard</h1>
  <div class="address">
    <svg class="icon" viewBox="0 0 12 12" style="margin-top:3px"><path d="M6 0C3.6 0 2 1.7 2 4c0 3 4 8 4 8s4-5 4-8c0-2.3-1.6-4-4-4z" fill="var(--orange)"/><circle cx="6" cy="4" r="1.4" fill="#fff"/></svg>
    <p>1187 North Cedar Row<br>Harbor Vale, CA. 90417</p>
  </div>

  <div class="divider"></div>

  <ul class="contact">
    <li><svg class="icon" viewBox="0 0 12 12"><path d="M2 1h3l1 3-2 1c.7 1.5 1.5 2.3 3 3l1-2 3 1v3c-6 0-9-3-9-9z" fill="var(--orange)"/></svg>000-0000-00000</li>
    <li><svg class="icon" viewBox="0 0 12 12"><rect x="1" y="2" width="10" height="8" rx="1" fill="var(--orange)"/><rect x="3" y="4" width="6" height="2" fill="#fff"/></svg>000-0000-00000</li>
    <li><svg class="icon" viewBox="0 0 12 12"><rect x="1" y="2.5" width="10" height="7" rx="1" fill="var(--orange)"/><path d="M1.5 3l4.5 3.5L10.5 3" stroke="#fff" fill="none"/></svg>Daltonpritchard@quillmail.com</li>
    <li><svg class="icon" viewBox="0 0 12 12"><circle cx="6" cy="6" r="5" fill="var(--orange)"/><path d="M1 6h10M6 1c-2 3-2 7 0 10M6 1c2 3 2 7 0 10" stroke="#fff" fill="none" stroke-width=".8"/></svg>www.sunnsailgrill.com</li>
  </ul>

  <svg class="bands" width="542" height="315" viewBox="0 0 542 315" aria-hidden="true">
    <defs>
      <linearGradient id="band-orange" x1="0" x2="1">
        <stop offset="0" stop-color="#f7a04a"/><stop offset="1" stop-color="#fde1bf"/>
      </linearGradient>
    </defs>
    <path d="M0 290H316L306 315H0Z" fill="url(#band-orange)"/>
    <path d="M330 272H542V315H312Z" fill="var(--navy)"/>
    <path d="M330 272H344L326 315H312Z" fill="var(--orange)"/>
  </svg>
</section>

</body>
</html>
```